Pelin Thai Massage Double Sided Flyer Luxury

I require a double sided flyer
we are a Thai Massage Spa
Would like gold, deep purple and bronze colours
Something eye catching and looks professional

```html
<!DOCTYPE html>
<html lang="en">
<head>
<meta charset="utf-8">
<title>Pelin Thai Massage – Double Sided Flyer</title>
<link rel="stylesheet" href="https://fonts.googleapis.com/css2?family=Cinzel:wght@400;500&family=Montserrat:wght@400;500;700;800&display=swap">
<style>
  :root {
    --canvas: #ececec;
    --ink: #080604;
    --panel: #0d0a06;
    --gold: #d6a63a;
    --gold-light: #f6d77e;
    --gold-deep: #9c6b1c;
    --bronze: #6b4516;
    --white: #ffffff;
    --text-soft: #f1ece2;
  }
  * { box-sizing: border-box; margin: 0; padding: 0; }
  html, body { width: 1200px; height: 2400px; overflow: hidden; }
  body {
    background: var(--canvas);
    font-family: "Montserrat", Arial, sans-serif;
    position: relative;
  }
  .flyer {
    position: absolute;
    left: 190px;
    width: 820px;
    height: 1160px;
    background: var(--ink);
    overflow: hidden;
    box-shadow: 0 6px 18px rgba(0,0,0,.28);
  }
  .flyer--front { top: 30px; }
  .flyer--back { top: 1210px; }

  .gold-text {
    background: linear-gradient(180deg, var(--gold-light) 0%, var(--gold) 45%, var(--gold-deep) 100%);
    -webkit-background-clip: text;
    background-clip: text;
    color: transparent;
  }

  /* ---------- Front ---------- */
  .hero-photo {
    position: absolute; inset: 0 0 auto 0; height: 880px;
    background:
      radial-gradient(ellipse 45% 35% at 70% 45%, #d9a174 0%, rgba(190,120,80,.7) 45%, transparent 75%),
      radial-gradient(ellipse 40% 30% at 25% 60%, #8a5a3a 0%, transparent 70%),
      radial-gradient(ellipse 50% 30% at 20% 90%, #e8e6e2 0%, transparent 70%),
      radial-gradient(ellipse 30% 45% at 85% 25%, #f2efe9 0%, transparent 70%),
      linear-gradient(160deg, #1a1208 0%, #4a3018 40%, #a07050 70%, #d8d2c8 100%);
  }
  .hero-glow {
    position: absolute; inset: 0 0 auto 0; height: 880px;
    background: radial-gradient(circle at 10% 10%, rgba(20,14,6,.85) 0%, transparent 40%);
  }
  .brand {
    position: absolute; left: 0; top: 60px; width: 314px;
    display: flex; flex-direction: column; align-items: center; gap: 16px;
  }
  .brand-dot {
    width: 82px; height: 82px; border-radius: 50%;
    border: 4px solid var(--gold);
  }
  .brand-name {
    font-family: "Montserrat", Arial, sans-serif;
    font-weight: 500; font-size: 22px; color: var(--gold);
    letter-spacing: .5px;
  }
  .front-panel { position: absolute; left: 0; top: 0; width: 820px; height: 1160px; }
  .detail-circle {
    position: absolute; border-radius: 50%;
    border: 7px solid var(--gold);
    box-shadow: 0 0 0 2px var(--gold-deep);
  }
  .detail-circle--herbal {
    left: 367px; top: 729px; width: 206px; height: 206px;
    background: radial-gradient(circle at 40% 35%, #b58ab8 0%, #6d4a70 25%, #2a2320 55%, #0f0c0a 100%);
  }
  .detail-circle--spa {
    left: 568px; top: 716px; width: 246px; height: 246px;
    background: radial-gradient(circle at 55% 65%, #f4f1ea 0%, #b9b3a6 25%, #4a3b2c 55%, #1a140e 100%);
  }
  .welcome {
    position: absolute; left: 57px; top: 880px;
    font-family: "Cinzel", "Times New Roman", serif; line-height: .95;
  }
  .welcome-small { display: block; font-size: 40px; letter-spacing: -.5px; }
  .welcome-large { display: block; font-size: 86px; letter-spacing: -2px; }
  .intro {
    position: absolute; left: 57px; top: 1022px; width: 722px;
    color: var(--text-soft); font-size: 12.5px; font-weight: 500; line-height: 1.3;
    text-align: justify;
  }
  .intro p + p { margin-top: 4px; }
  .web-line {
    position: absolute; left: 0; right: 0; top: 1112px; text-align: center;
    font-size: 14px; font-weight: 700; letter-spacing: 3.5px; color: var(--white);
  }
  .web-line .accent { color: var(--gold); }

  /* ---------- Back ---------- */
  .back-glow {
    position: absolute; inset: 0;
    background:
      radial-gradient(circle at 95% 15%, rgba(214,166,58,.45) 0%, transparent 30%),
      radial-gradient(circle at 90% 65%, rgba(214,166,58,.25) 0%, transparent 30%),
      radial-gradient(circle at 30% 70%, rgba(107,69,22,.18) 0%, transparent 45%);
  }
  .back-arc { position: absolute; inset: 0; }
  .services-title {
    position: absolute; left: 55px; top: 72px;
    font-family: "Cinzel", "Times New Roman", serif; font-size: 71px; line-height: 1;
    letter-spacing: -1px;
  }
  .services-lede {
    position: absolute; left: 55px; top: 172px; width: 372px;
    color: var(--white); font-size: 12.5px; font-weight: 700; line-height: 1.3;
    text-align: justify;
  }
  .menu-heading {
    position: absolute; left: 55px; top: 272px;
    font-family: "Cinzel", "Times New Roman", serif; font-size: 43px; color: var(--white);
    line-height: 1;
  }
  .menu-group { position: absolute; left: 55px; width: 400px; }
  .menu-group--deep { top: 346px; }
  .menu-group--floor { top: 650px; }
  .menu-tag {
    display: inline-block; height: 50px; line-height: 50px; padding: 0 24px;
    background: linear-gradient(180deg, var(--gold-light), var(--gold) 50%, var(--gold-deep));
    color: var(--ink); font-weight: 800; font-size: 17px; letter-spacing: .3px;
  }
  .menu-group--deep .menu-tag { width: 293px; }
  .menu-group--floor .menu-tag { width: 389px; padding: 0 22px; font-size: 16.5px; }
  .menu-item { position: relative; width: 360px; margin-top: 26px; }
  .menu-item + .menu-item { margin-top: 30px; }
  .menu-duration, .menu-price {
    color: var(--gold); font-weight: 700; font-size: 25px; line-height: 1;
  }
  .menu-price { position: absolute; right: 0; top: 0; }
  .menu-desc {
    margin-top: 6px; width: 250px;
    color: var(--white); font-size: 17.5px; line-height: 1.5;
  }
  .voucher {
    position: absolute; left: 58px; top: 856px; width: 253px; height: 68px;
    border-top: 7px solid var(--gold); border-bottom: 7px solid var(--gold);
    border-left: 3px solid var(--gold-deep);
    display: flex; align-items: center; gap: 18px; padding-left: 22px;
  }
  .voucher-dot {
    width: 66px; height: 66px; border-radius: 50%; flex: none;
    background: radial-gradient(circle at 35% 30%, var(--gold-light), var(--gold) 55%, var(--gold-deep));
    margin-top: -1px;
  }
  .voucher-text {
    color: var(--white); font-weight: 800; font-size: 12.5px; line-height: 1.05;
  }
  .contact {
    position: absolute; left: 55px; top: 1018px;
    list-style: none; color: var(--white); font-size: 18px; line-height: 1.4;
  }
  .contact li { display: flex; gap: 10px; align-items: flex-start; }
  .contact svg { flex: none; margin-top: 4px; }
  .contact .indent { padding-left: 28px; }
  .service-photo {
    position: absolute; border-radius: 50%;
    border: 7px solid var(--gold);
    box-shadow: 0 0 0 2px var(--gold-deep);
  }
  .service-photo--deep {
    left: 473px; top: 221px; width: 298px; height: 298px;
    background: radial-gradient(ellipse at 45% 55%, #c98e62 0%, #8f5e3c 40%, #e9e3da 75%, #d9d0c2 100%);
  }
  .service-photo--relax {
    left: 475px; top: 509px; width: 332px; height: 332px;
    background: radial-gradient(ellipse at 50% 50%, #ead9cc 0%, #c9a998 30%, #2a1c16 60%, #f1ece6 100%);
  }
  .service-photo--facial {
    left: 458px; top: 825px; width: 280px; height: 280px;
    background: radial-gradient(ellipse at 55% 45%, #f2e7df 0%, #e3cfc2 40%, #f8f5f1 80%);
  }
</style>
</head>
<body>

<section class="flyer flyer--front" aria-label="Flyer front">
  <div class="hero-photo" role="img" aria-label="Photo of a therapist giving a relaxing back massage to a client lying on a white towel, with frangipani flowers and spa spices"></div>
  <div class="hero-glow"></div>

  <div class="brand">
    <span class="brand-dot"></span>
    <span class="brand-name">Pelin Thai Massage</span>
  </div>

  <svg class="front-panel" viewBox="0 0 820 1160" aria-hidden="true">
    <defs>
      <linearGradient id="goldStroke" x1="0" x2="1">
        <stop offset="0" stop-color="#9c6b1c"/>
        <stop offset=".5" stop-color="#f6d77e"/>
        <stop offset="1" stop-color="#d6a63a"/>
      </linearGradient>
    </defs>
    <path d="M0 858 Q220 818 430 818 L820 800 L820 1160 L0 1160 Z" fill="#080604"/>
    <path d="M0 858 Q220 818 430 818" fill="none" stroke="url(#goldStroke)" stroke-width="7"/>
  </svg>

  <div class="detail-circle detail-circle--herbal" role="img" aria-label="Photo of a purple herbal compress with black hot stones"></div>
  <div class="detail-circle detail-circle--spa" role="img" aria-label="Photo of white herbal compresses and frangipani flowers"></div>

  <h1 class="welcome gold-text">
    <span class="welcome-small">Welcome to</span>
    <span class="welcome-large">Luxury</span>
  </h1>

  <div class="intro">
    <p>Set in the heart of Roundhay, Pelin Thai Massage will allow you to immerse yourself in a place where your wellbeing and rejuvenation is at the centre of what we do.</p>
    <p>Using Thai traditions, our highly trained therapists offer revitalising body treatments with their deep tissue massage techniques. In their hands, you will see and feel immediate results.</p>
  </div>

  <p class="web-line">WWW.<span class="accent">PELINTHAIMASSAGE</span>.CO.UK</p>
</section>

<section class="flyer flyer--back" aria-label="Flyer back">
  <div class="back-glow"></div>
  <svg class="back-arc" viewBox="0 0 820 1160" aria-hidden="true">
    <defs>
      <linearGradient id="arcGold" x1="0" y1="0" x2="0" y2="1">
        <stop offset="0" stop-color="#f6d77e"/>
        <stop offset=".5" stop-color="#d6a63a"/>
        <stop offset="1" stop-color="#f6d77e"/>
      </linearGradient>
    </defs>
    <path d="M500 0 Q430 260 470 520 Q510 860 520 1160" fill="none" stroke="url(#arcGold)" stroke-width="9"/>
  </svg>

  <h2 class="services-title gold-text">Massages</h2>
  <p class="services-lede">Restore balance. Revive your senses. Discover all the ways Pelin Thai Massage can breathe new life into your body and soul.</p>

  <h3 class="menu-heading">Massages</h3>

  <div class="menu-group menu-group--deep">
    <span class="menu-tag">DEEP TISSUE MASSAGE</span>
    <div class="menu-item">
      <span class="menu-duration">60 minutes</span><span class="menu-price">£45</span>
      <p class="menu-desc">Oil massage personalised, light to firm pressure</p>
    </div>
    <div class="menu-item">
      <span class="menu-duration">90 minutes</span><span class="menu-price">£55</span>
      <p class="menu-desc">Oil massage, medium to firm pressure</p>
    </div>
  </div>

  <div class="menu-group menu-group--floor">
    <span class="menu-tag">THAI FLOOR TRADTIONAL MASSAGE</span>
    <div class="menu-item">
      <span class="menu-duration">60 minutes</span><span class="menu-price">£45</span>
      <p class="menu-desc" style="width:290px">Dry massage, medium to firm pressure applying stretching technique</p>
    </div>
  </div>

  <div class="voucher">
    <span class="voucher-dot"></span>
    <span class="voucher-text">GIFT VOUCHERS<br>AVAILABLE</span>
  </div>

  <ul class="contact">
    <li>
      <svg width="16" height="18" viewBox="0 0 16 20"><path d="M8 0a7 7 0 0 0-7 7c0 5 7 13 7 13s7-8 7-13a7 7 0 0 0-7-7zm0 10a3 3 0 1 1 0-6 3 3 0 0 1 0 6z" fill="#d6a63a"/></svg>
      <span>Pelin Thai Massage</span>
    </li>
    <li class="indent">12 Willow Road Leeds LS0 4QT</li>
    <li>
      <svg width="17" height="17" viewBox="0 0 20 20"><circle cx="10" cy="10" r="10" fill="#d6a63a"/><path d="M6.5 5.5l2 0 1 2.5-1.3 1a6 6 0 0 0 2.8 2.8l1-1.3 2.5 1v2a1 1 0 0 1-1 1A8 8 0 0 1 5.5 6.5a1 1 0 0 1 1-1z" fill="#0d0a06"/></svg>
      <span>0113 4960712</span>
    </li>
    <li>
      <svg width="17" height="17" viewBox="0 0 20 20"><circle cx="10" cy="10" r="8.5" fill="none" stroke="#d6a63a" stroke-width="2"/><ellipse cx="10" cy="10" rx="3.5" ry="8.5" fill="none" stroke="#d6a63a" stroke-width="1.6"/><path d="M1.5 10h17M3 5.5h14M3 14.5h14" stroke="#d6a63a" stroke-width="1.4"/></svg>
      <span>www.pelinthaimassage.co.uk</span>
    </li>
  </ul>

  <div class="service-photo service-photo--deep" role="img" aria-label="Photo of a man relaxing during a shoulder massage beside candles"></div>
  <div class="service-photo service-photo--relax" role="img" aria-label="Photo of a woman resting with flowers in her hair"></div>
  <div class="service-photo service-photo--facial" role="img" aria-label="Photo of a client receiving a facial treatment with a head towel"></div>
</section>

</body>
</html>
```